the theater production needs a poster design

we need a poster design for a theater drama in Seoul , South Korea.

the title : THE LANTERN KEEPER'S ROAD
BASED ON WALTER DREVICK'S BOOK

where:Haneulbit Stagehouse, Jongro-Gu, Seoul
when:2022.1.1~OpenRun
Saturday 3PM, 63PM, Sunday 5pm, Monday 7:30pm

TICKET PRICE: $45

BOOK NOW
02 471 6039
RIVA TROUPE

Director Minha Park Composer Sora Lee, Sound Director Doyun Han
Producer Taesik Yoon

Target Market(s)

for Chiristan and others

Industry/Entity Type

Christian community and non Christian society

Colors
0094D4
00A9DD
6FCCEA
C7EBF8
E9F6FB

Requirements
Must have
• the main Character, pilgrim should should carry some burdens on his shoulder

```html
<!DOCTYPE html>
<html lang="en">
<head>
<meta charset="utf-8">
<title>The Lantern Keeper's Road — Theatre Poster</title>
<link href="https://fonts.googleapis.com/css2?family=Cormorant+Garamond:wght@500&family=Oswald:wght@300;400;500&display=swap" rel="stylesheet">
<style>
  :root {
    --sky-deep: #0094D4;
    --sky: #00A9DD;
    --sky-soft: #6FCCEA;
    --sky-pale: #C7EBF8;
    --mist: #E9F6FB;
    --navy: #17255e;
    --navy-ink: #121a36;
    --gold: #b29470;
    --white: #ffffff;
    --bar: rgba(18, 26, 60, 0.75);
  }
  html, body {
    margin: 0;
    padding: 0;
    width: 720px;
    height: 1200px;
    overflow: hidden;
    background: var(--mist);
  }
  .poster {
    position: relative;
    width: 720px;
    height: 1200px;
    overflow: hidden;
    font-family: "Oswald", "Arial Narrow", sans-serif;
    color: var(--white);
    background: linear-gradient(180deg,
      #ffffff 0%,
      var(--mist) 7%,
      var(--sky-soft) 20%,
      var(--sky-deep) 42%,
      #1a7fd0 62%,
      #1f4a9c 80%,
      var(--navy) 100%);
  }
  .source-line {
    position: absolute;
    top: 32px;
    left: 0;
    width: 100%;
    margin: 0;
    text-align: center;
    font-size: 21px;
    font-weight: 400;
    color: var(--gold);
    letter-spacing: 0.5px;
  }
  .title {
    position: absolute;
    top: 78px;
    left: 0;
    width: 100%;
    margin: 0;
    text-align: center;
    font-family: "Cormorant Garamond", "Times New Roman", serif;
    font-weight: 500;
    font-size: 78px;
    line-height: 1.12;
    color: var(--navy-ink);
    letter-spacing: 1px;
  }
  .title .line-two { display: block; color: #2b2f45; }
  .pilgrim-photo {
    position: absolute;
    left: 170px;
    top: 300px;
    width: 400px;
    height: 680px;
    border-radius: 180px 180px 20px 20px;
    background: radial-gradient(ellipse at 50% 35%, #d8c4a4 0%, #a8895f 30%, rgba(80, 110, 150, 0.7) 65%, rgba(30, 110, 200, 0) 100%);
  }
  .feather {
    position: absolute;
    border-radius: 50%;
    background: linear-gradient(135deg, rgba(255,255,255,0.9), rgba(255,255,255,0.2));
  }
  .feather-top { left: 12px; top: 290px; width: 92px; height: 36px; transform: rotate(40deg); }
  .feather-bottom { right: 4px; top: 1125px; width: 96px; height: 34px; transform: rotate(-48deg); }
  .flare {
    position: absolute;
    left: 210px;
    top: 945px;
    width: 220px;
    height: 18px;
    border-radius: 50%;
    background: radial-gradient(ellipse, rgba(255,230,170,0.95) 0%, rgba(255,170,80,0.5) 35%, rgba(255,170,80,0) 70%);
  }
  .opening {
    position: absolute;
    left: 0;
    top: 560px;
    width: 175px;
  }
  .opening-tag {
    background: var(--white);
    color: #2c5fb8;
    font-size: 27px;
    font-weight: 500;
    text-align: right;
    padding: 0 20px 0 0;
    width: 145px;
    height: 34px;
    line-height: 34px;
    margin-left: 10px;
  }
  .opening-rule { height: 2px; background: var(--white); width: 175px; }
  .opening-date {
    margin: 12px 0 0 26px;
    font-size: 44px;
    font-weight: 500;
    line-height: 1;
  }
  .opening-run {
    margin: 6px 0 12px 30px;
    font-size: 28px;
    font-weight: 400;
    line-height: 1;
  }
  .booking {
    position: absolute;
    right: 48px;
    top: 890px;
    width: 104px;
    text-align: center;
  }
  .booking-phone { font-size: 19px; font-weight: 300; white-space: nowrap; }
  .booking-cta {
    margin-top: 4px;
    border: 2px solid var(--sky-pale);
    font-size: 22px;
    font-weight: 500;
    color: var(--sky-pale);
    line-height: 30px;
    white-space: nowrap;
  }
  .booking-price {
    margin-top: 4px;
    border: 2px solid var(--sky-pale);
    color: var(--sky-pale);
    padding: 2px 0 6px;
  }
  .booking-price-label { font-size: 17px; font-weight: 300; }
  .booking-price-amount { font-size: 62px; font-weight: 300; line-height: 0.95; }
  .booking-price-amount small { font-size: 32px; font-weight: 500; }
  .venue {
    position: absolute;
    left: 56px;
    top: 995px;
    width: 490px;
    font-size: 19px;
    font-weight: 300;
    letter-spacing: 3.5px;
    white-space: nowrap;
  }
  .showtimes {
    position: absolute;
    left: 48px;
    top: 1030px;
    width: 500px;
    height: 44px;
    line-height: 44px;
    background: var(--bar);
    border-top: 1px solid rgba(255,255,255,0.25);
    font-size: 22px;
    font-weight: 300;
    padding-left: 10px;
    box-sizing: border-box;
    white-space: nowrap;
  }
  .showtimes .sep { margin: 0 9px; }
  .credits-rule {
    position: absolute;
    left: 48px;
    top: 1098px;
    width: 620px;
    height: 1px;
    background: rgba(255,255,255,0.55);
  }
  .credits {
    position: absolute;
    left: 48px;
    top: 1114px;
    width: 560px;
    text-align: center;
    font-size: 17px;
    font-weight: 300;
    line-height: 30px;
    white-space: nowrap;
  }
  .credits b { font-weight: 500; }
  .credits .sep { margin: 0 8px; }
</style>
</head>
<body>
<main class="poster">
  <p class="source-line">BASED ON WALTER DREVICK'S BOOK</p>
  <h1 class="title">THE LANTERN<span class="line-two">KEEPER'S ROAD</span></h1>

  <div class="pilgrim-photo" role="img" aria-label="Pilgrim walking down an old Seoul alley, carrying a large bundle of burdens on his back and shoulders"></div>
  <div class="feather feather-top" role="img" aria-label="White feather"></div>
  <div class="feather feather-bottom" role="img" aria-label="White feather"></div>
  <div class="flare"></div>

  <section class="opening">
    <div class="opening-tag">OPEN DOOR</div>
    <div class="opening-rule"></div>
    <div class="opening-date">2022.1.1</div>
    <div class="opening-run">~ OPEN RUN</div>
    <div class="opening-rule"></div>
  </section>

  <section class="booking">
    <div class="booking-phone">+02 471 6039</div>
    <div class="booking-cta">BOOK NOW</div>
    <div class="booking-price">
      <div class="booking-price-label">ENTRY</div>
      <div class="booking-price-amount">45<small>$</small></div>
    </div>
  </section>

  <div class="venue">HANEULBIT STAGEHOUSE, JONGRO-GU, SEOUL</div>
  <div class="showtimes">Saturday 3:00 pm<span class="sep">|</span>Sunday 5:00 pm<span class="sep">|</span>Monday 7:30 pm</div>

  <div class="credits-rule"></div>
  <div class="credits">
    <b>DIRECTOR:</b> MINHA PARK<span class="sep">|</span><b>COMPOSER:</b> SORA LEE<span class="sep">|</span><b>SOUND DIRECTOR:</b> DOYUN HAN<br>
    <b>PRODUCER:</b> TAESIK YOON<span class="sep">|</span><b>RIVA TROUPE</b>
  </div>
</main>
</body>
</html>
```